HIGH END CRAFT BEER LINE EXTENSION

We are planning to launch 2 new beers in a "Signature Series" line extension for the Maurice-Olivier craft beer line. The beer will need to use the same brand name and logo, but have a completely different packaging. The bottle will be 750 ml (picture of bottle attached) and have a different shape than the current bottle that contains 500 ml.

Target Market(s)

High-End Wealthy Customers. Mostly males.

Requirements
Must have
• High end "classy" design. This beer will be the most expensive beer in the store. It will be as expensive as wine. It needs to look expensive, elegant and formal.
• It needs to use the same logo as the current line-up.
Nice to have
• We will have 2 flavours. "Belgium Quadrupel" and "Baltic Porter"
• It needs to integrate the "Signature Series" information on the front label and have the potential to add other flavours in the future.

```html
<!DOCTYPE html>
<html lang="fr">
<head>
<meta charset="utf-8">
<title>Maurice-Olivier — Belgium Quadrupel label</title>
<link rel="stylesheet" href="https://fonts.googleapis.com/css2?family=Oswald:wght@600&family=Roboto+Slab:wght@700&family=Cinzel:wght@500&display=swap">
<style>
  :root {
    --backdrop: #efede6;
    --label-black: #151513;
    --ring-dark: #22211d;
    --gold: #c9a635;
    --gold-soft: #8c7a3e;
    --cream: #f3efe2;
  }
  * { margin: 0; padding: 0; box-sizing: border-box; }
  html, body {
    width: 802px;
    height: 1200px;
    overflow: hidden;
    background: var(--backdrop);
  }
  .label {
    position: relative;
    width: 802px;
    height: 1200px;
  }
  .label-shape {
    position: absolute;
    inset: 0;
  }
  .label-text {
    position: absolute;
    left: 0;
    width: 100%;
    text-align: center;
  }
  .brand-name {
    top: 452px;
    font-family: "Oswald", sans-serif;
    font-weight: 600;
    font-size: 100px;
    line-height: 104px;
    letter-spacing: 4px;
    color: var(--gold);
  }
  .flavour {
    top: 684px;
    font-family: "Roboto Slab", serif;
    font-weight: 700;
    font-size: 34px;
    letter-spacing: 3px;
    color: var(--cream);
  }
  .origin {
    top: 738px;
    font-family: "Cinzel", serif;
    font-weight: 500;
    font-size: 22px;
    letter-spacing: 3px;
    color: var(--gold);
  }
</style>
</head>
<body>
  <main class="label">
    <svg class="label-shape" width="802" height="1200" viewBox="0 0 802 1200" aria-hidden="false">
      <ellipse class="outer-edge" cx="401" cy="600" rx="304" ry="404" fill="var(--gold-soft)"/>
      <ellipse class="outer-ring" cx="401" cy="600" rx="298" ry="398" fill="var(--ring-dark)"/>
      <ellipse class="ring-line" cx="401" cy="600" rx="284" ry="383" fill="none" stroke="var(--gold-soft)" stroke-width="3" stroke-dasharray="2 8" stroke-linecap="round"/>
      <ellipse class="inner-edge" cx="401" cy="600" rx="268" ry="366" fill="var(--gold)"/>
      <ellipse class="label-field" cx="401" cy="600" rx="264" ry="362" fill="var(--label-black)"/>
      <defs>
        <linearGradient id="ornament-tone" x1="0" x2="1" y1="0" y2="0">
          <stop offset="0" stop-color="#151513"/>
          <stop offset="0.5" stop-color="#9a8a55"/>
          <stop offset="1" stop-color="#151513"/>
        </linearGradient>
      </defs>
      <rect class="ornament-top" x="281" y="318" width="240" height="100" rx="20" fill="url(#ornament-tone)" opacity="0.55" role="img" aria-label="Fine engraved scroll flourish above the brand name"/>
      <rect class="ornament-bottom" x="291" y="790" width="220" height="80" rx="20" fill="url(#ornament-tone)" opacity="0.55" role="img" aria-label="Fine engraved scroll flourish below the origin line"/>
    </svg>

    <h1 class="label-text brand-name">MAURICE<br>OLIVIER</h1>
    <p class="label-text flavour">BELGIUM QUADRUPEL</p>
    <p class="label-text origin">BRASSÉE AU QUÉBEC</p>
  </main>
</body>
</html>
```